Fitness Nutrition Book to be designed

My business is an Online Fitness Training Business.
I have created a nutritional booklet that each online client will receive.
The booklet in total is 17 pages, which includes front and back cover.
Text has all been completed.
The booklet should be easy to read and using colors that convey energy, such as blues, blacks, greys, yellows, reds, etc.
I do not have photos of clients working out, but I would like to use photos that represent fitness.
Appropriate items would be Kettle Bells, Dumbbells, Battle Ropes and Slam balls
I would like the interior pages to have motivational quotes, creatively and eye catching, placed on the pages.
Quotes such as:
"If it doesn't challenge you, It wont change you!"
"Train insane or remain the same"
"Sweat is Fat Crying"
"Sore Today Strong Tomorrow"
"Motivation is what gets you started, Habit is what keeps you going"
"3 Months from now you will thank yourself"
These are all quotes that I found from googling "Motivational Fitness Quote Images."
The cover should contain our            PulvaCore logo.
with                                 "You are a part of the fitness revolution!"
Meal Plan
The only interior page that will change is the meal plan portion.
There are 5 different meal plans, 1200, 1500, 1750, 2000 & 2200 calories
I would also like the correct caloric number of the interior meal plan to be placed somewhere on the cover page as well, so that by looking at the cover page, the 1200 calorie meal plan book would be easily found and distinguishable from the 1500 calorie meal plan book.
Thank you!

Updates
Project Deadline Extended Reason: Revised project description to make more clear for designers. Initial description was very vague Added Wednesday, August 30, 2017
Target Market(s)
Target market:
25-45 year old
60% female / 40% male
has at least one child
middle income
Gets coffee at brewlanes
States that they, "want to tone up"
Currently goes to the gym maybe 1-3 x per week
Industry/Entity Type
Business
Requirements
Must have
- Clear, easy to read and follow
- I have included a file labeled "Competitors Example" This is one of my old packets that I had made years ago. I do not like this style of cover with tons of pictures
- And the new packet I am wanting to have created should look much better.

Should not have
- This packet should not be plain and boring. There should not be any page that is simply white with small black text.

```html
<!DOCTYPE html>
<html lang="en">
<head>
<meta charset="utf-8">
<title>PulvaCore Meal Plan Covers</title>
<link href="https://fonts.googleapis.com/css2?family=Barlow+Condensed:ital,wght@0,500;0,600;0,700;1,500;1,700&family=Open+Sans:wght@400&display=swap" rel="stylesheet">
<style>
  :root {
    --board: #4a4a4c;
    --tab: #1e73be;
    --cover-dark: #0d0f14;
    --photo-warm: #3a2a22;
    --photo-deep: #1a1517;
    --ink: #ffffff;
    --lime: #c8d92b;
    --blue: #1f6fd0;
    --blue-2: #3d7fe0;
    --red: #f0452a;
    --red-2: #f25a2c;
    --green: #7cc242;
    --green-2: #d4e021;
    --purple: #9b1f9a;
    --purple-2: #e02a9c;
    --orange: #f7921e;
    --orange-2: #f9a51f;
  }
  * { box-sizing: border-box; margin: 0; padding: 0; }
  html, body { width: 1200px; height: 1200px; overflow: hidden; }
  body { background: var(--board); position: relative; font-family: "Barlow Condensed", sans-serif; }

  .section-tab {
    position: absolute; left: 538px; top: 0; width: 124px; height: 70px;
    background: var(--tab); color: var(--ink);
    font: 400 26px/70px "Open Sans", sans-serif; text-align: center;
  }

  .cover {
    position: absolute; width: 371px; height: 479px; overflow: hidden;
    background: var(--cover-dark);
    box-shadow: 0 2px 6px rgba(0,0,0,.45);
  }
  .cover--1200 { left: 217px; top: 147px; --accent: var(--blue);   --accent-2: var(--blue-2); }
  .cover--1500 { left: 613px; top: 147px; --accent: var(--red);    --accent-2: var(--red-2); }
  .cover--1750 { left: 31px;  top: 674px; --accent: var(--green);  --accent-2: var(--green-2); }
  .cover--2000 { left: 414px; top: 674px; --accent: var(--purple); --accent-2: var(--purple-2); }
  .cover--2200 { left: 798px; top: 674px; --accent: var(--orange); --accent-2: var(--orange-2); }

  .athlete-photo {
    position: absolute; right: 0; top: 0; width: 210px; height: 479px;
    background: linear-gradient(90deg, var(--cover-dark) 0%, var(--photo-deep) 35%, var(--photo-warm) 100%);
  }

  .accent-shapes { position: absolute; left: 0; top: 0; width: 371px; height: 479px; }
  .accent-shapes .shape-main { fill: var(--accent); }
  .accent-shapes .shape-alt { fill: var(--accent-2); }

  .brand { position: absolute; left: 24px; top: 32px; color: var(--ink); }
  .brand__name { font-weight: 700; font-size: 44px; line-height: 1; letter-spacing: .5px; }
  .brand__tagline { font: 400 9px/1 "Open Sans", sans-serif; letter-spacing: 2px; margin-top: 4px; }

  .rule { position: absolute; left: 0; height: 2px; background: var(--lime); }
  .rule--top { top: 121px; width: 78px; }
  .rule--bottom { top: 301px; width: 194px; }

  .slogan {
    position: absolute; left: 26px; top: 134px;
    font-style: italic; font-weight: 500; font-size: 37px; line-height: 40px;
    color: var(--ink); text-transform: uppercase; letter-spacing: -.3px;
  }
  .slogan__strong { color: var(--lime); font-weight: 700; display: block; }

  .plan-title {
    position: absolute; left: 23px; top: 356px;
    font-weight: 700; font-size: 52px; line-height: 1; color: var(--ink);
    letter-spacing: -.5px; white-space: nowrap;
    transform: scaleX(.84); transform-origin: left top;
  }
  .calorie-badge {
    position: absolute; left: 24px; top: 403px; width: 160px; height: 34px;
    background: var(--accent); color: var(--ink);
    font-weight: 500; font-size: 24px; line-height: 34px; text-align: center; letter-spacing: 1.5px;
  }
</style>
</head>
<body>
  <div class="section-tab">COVERS</div>

  <div class="cover cover--1200">
    <div class="athlete-photo" role="img" aria-label="Photo area: athlete in a sports top"></div>
    <svg class="accent-shapes" viewBox="0 0 371 479" aria-hidden="true">
      <polygon class="shape-main" points="0,320 371,440 371,479 0,479" opacity=".55"/>
      <polygon class="shape-main" points="0,400 371,360 371,479 0,479" opacity=".6"/>
      <polygon class="shape-alt" points="120,479 371,400 371,479" opacity=".9"/>
      <polygon class="shape-main" points="0,440 200,479 0,479" opacity=".8"/>
    </svg>
    <div class="brand"><div class="brand__name">PulvaCore</div><div class="brand__tagline">Online Fitness Coaching</div></div>
    <div class="rule rule--top"></div>
    <div class="slogan">You are<br>a part of<span class="slogan__strong">the fitness</span><span class="slogan__strong">revolution!</span></div>
    <div class="rule rule--bottom"></div>
    <div class="plan-title">MEAL PLAN</div>
    <div class="calorie-badge">1200 CALORIES</div>
  </div>

  <div class="cover cover--1500">
    <div class="athlete-photo" role="img" aria-label="Photo area: athlete in a sports top"></div>
    <svg class="accent-shapes" viewBox="0 0 371 479" aria-hidden="true">
      <polygon class="shape-main" points="0,320 371,440 371,479 0,479" opacity=".55"/>
      <polygon class="shape-main" points="0,400 371,360 371,479 0,479" opacity=".6"/>
      <polygon class="shape-alt" points="120,479 371,400 371,479" opacity=".9"/>
      <polygon class="shape-main" points="0,440 200,479 0,479" opacity=".8"/>
    </svg>
    <div class="brand"><div class="brand__name">PulvaCore</div><div class="brand__tagline">Online Fitness Coaching</div></div>
    <div class="rule rule--top"></div>
    <div class="slogan">You are<br>a part of<span class="slogan__strong">the fitness</span><span class="slogan__strong">revolution!</span></div>
    <div class="rule rule--bottom"></div>
    <div class="plan-title">MEAL PLAN</div>
    <div class="calorie-badge">1500 CALORIES</div>
  </div>

  <div class="cover cover--1750">
    <div class="athlete-photo" role="img" aria-label="Photo area: athlete in a sports top"></div>
    <svg class="accent-shapes" viewBox="0 0 371 479" aria-hidden="true">
      <polygon class="shape-main" points="0,320 371,440 371,479 0,479" opacity=".55"/>
      <polygon class="shape-main" points="0,400 371,360 371,479 0,479" opacity=".6"/>
      <polygon class="shape-alt" points="120,479 371,400 371,479" opacity=".9"/>
      <polygon class="shape-main" points="0,440 200,479 0,479" opacity=".8"/>
    </svg>
    <div class="brand"><div class="brand__name">PulvaCore</div><div class="brand__tagline">Online Fitness Coaching</div></div>
    <div class="rule rule--top"></div>
    <div class="slogan">You are<br>a part of<span class="slogan__strong">the fitness</span><span class="slogan__strong">revolution!</span></div>
    <div class="rule rule--bottom"></div>
    <div class="plan-title">MEAL PLAN</div>
    <div class="calorie-badge">1750 CALORIES</div>
  </div>

  <div class="cover cover--2000">
    <div class="athlete-photo" role="img" aria-label="Photo area: athlete in a sports top"></div>
    <svg class="accent-shapes" viewBox="0 0 371 479" aria-hidden="true">
      <polygon class="shape-main" points="0,320 371,440 371,479 0,479" opacity=".55"/>
      <polygon class="shape-main" points="0,400 371,360 371,479 0,479" opacity=".6"/>
      <polygon class="shape-alt" points="120,479 371,400 371,479" opacity=".9"/>
      <polygon class="shape-main" points="0,440 200,479 0,479" opacity=".8"/>
    </svg>
    <div class="brand"><div class="brand__name">PulvaCore</div><div class="brand__tagline">Online Fitness Coaching</div></div>
    <div class="rule rule--top"></div>
    <div class="slogan">You are<br>a part of<span class="slogan__strong">the fitness</span><span class="slogan__strong">revolution!</span></div>
    <div class="rule rule--bottom"></div>
    <div class="plan-title">MEAL PLAN</div>
    <div class="calorie-badge">2000 CALORIES</div>
  </div>

  <div class="cover cover--2200">
    <div class="athlete-photo" role="img" aria-label="Photo area: athlete in a sports top"></div>
    <svg class="accent-shapes" viewBox="0 0 371 479" aria-hidden="true">
      <polygon class="shape-main" points="0,320 371,440 371,479 0,479" opacity=".55"/>
      <polygon class="shape-main" points="0,400 371,360 371,479 0,479" opacity=".6"/>
      <polygon class="shape-alt" points="120,479 371,400 371,479" opacity=".9"/>
      <polygon class="shape-main" points="0,440 200,479 0,479" opacity=".8"/>
    </svg>
    <div class="brand"><div class="brand__name">PulvaCore</div><div class="brand__tagline">Online Fitness Coaching</div></div>
    <div class="rule rule--top"></div>
    <div class="slogan">You are<br>a part of<span class="slogan__strong">the fitness</span><span class="slogan__strong">revolution!</span></div>
    <div class="rule rule--bottom"></div>
    <div class="plan-title">MEAL PLAN</div>
    <div class="calorie-badge">2200 CALORIES</div>
  </div>
</body>
</html>
```